July 4th Postcard to existing clients

5x7 postcard wishing our clients happy 4th of July. Card should read on the back "Thank You For Being A Valued Client!. Stay Safe And Enjoy Your Independence Day Celebrations!"

Patriotic theme with fireworks is ideal. We are a law firm so should still have a feel of professionalism while still being fun since it is for a fun holiday.

```html
<!DOCTYPE html>
<html lang="en">
<head>
<meta charset="utf-8">
<title>Brightwater Legal – Independence Day Postcard</title>
<link rel="stylesheet" href="https://fonts.googleapis.com/css2?family=Oswald:wght@500;700&family=Roboto+Condensed:wght@700&display=swap">
<style>
  :root {
    --page-bg: #d9d9db;
    --card-white: #ffffff;
    --panel-grey: #ebebec;
    --brand-blue: #3c58a6;
    --brand-red: #e1262a;
    --line-grey: #8a8a8a;
    --photo-deep: #27377e;
    --photo-violet: #6c4fa0;
    --photo-pink: #c772b4;
  }
  * { margin: 0; padding: 0; box-sizing: border-box; }
  html, body { width: 874px; height: 1200px; overflow: hidden; }
  body { background: var(--page-bg); position: relative; font-family: "Roboto Condensed", sans-serif; }

  .postcard {
    position: absolute;
    left: 82px;
    width: 710px;
    background: var(--card-white);
    overflow: hidden;
    box-shadow: 0 2px 6px rgba(0,0,0,.18);
  }
  .postcard--front { top: 76px; height: 507px; }
  .postcard--back { top: 617px; height: 508px; }
  .postcard__art { position: absolute; inset: 0; width: 100%; height: 100%; display: block; }

  .brand {
    position: absolute;
    display: flex; align-items: center; justify-content: center; gap: 10px;
    color: var(--brand-blue);
  }
  .brand__dot { flex: none; border-radius: 50%; background: var(--brand-red); }
  .brand__name { font-family: "Oswald", sans-serif; font-weight: 500; line-height: 1; white-space: nowrap; }

  .postcard--front .brand { left: 388px; top: 92px; width: 240px; height: 40px; }
  .postcard--front .brand__dot { width: 14px; height: 14px; }
  .postcard--front .brand__name { font-size: 29px; }

  .postcard--back .brand { left: 22px; top: 98px; width: 210px; height: 34px; }
  .postcard--back .brand__dot { width: 12px; height: 12px; }
  .postcard--back .brand__name { font-size: 24px; }

  .greeting {
    position: absolute; left: 300px; top: 376px; width: 370px;
    text-align: center; color: #fff;
    font-family: "Oswald", sans-serif; font-weight: 700; line-height: 1;
  }
  .greeting__line--small { display: block; font-size: 47px; }
  .greeting__line--large { display: block; font-size: 55px; margin-top: 8px; letter-spacing: .5px; }

  .thanks { position: absolute; left: 37px; top: 176px; width: 260px; font-family: "Roboto Condensed", sans-serif; font-weight: 700; color: var(--brand-blue); }
  .thanks__title { font-size: 60px; line-height: 1; }
  .thanks__sub { font-size: 20px; line-height: 1; margin-top: 9px; }

  .wish {
    position: absolute; left: 34px; top: 288px; width: 250px; height: 62px;
    border: 1.5px solid var(--brand-red); border-radius: 7px; background: #fff;
    display: flex; align-items: center; justify-content: center; text-align: center;
    font-family: "Roboto Condensed", sans-serif; font-weight: 700; font-size: 16px; line-height: 1.15; color: var(--brand-red);
  }

  .stamp-box { position: absolute; left: 572px; top: 45px; width: 109px; height: 107px; border: 1.5px solid #555; }
  .address-line { position: absolute; left: 388px; width: 292px; height: 0; border-top: 1.5px solid var(--line-grey); }
  .address-line--1 { top: 313px; }
  .address-line--2 { top: 350px; }
  .address-line--3 { top: 387px; }
</style>
</head>
<body>

<section class="postcard postcard--front" aria-label="Postcard front">
  <svg class="postcard__art" viewBox="0 0 503 359" preserveAspectRatio="none">
    <defs>
      <linearGradient id="photoTone" x1="0" y1="0" x2="0.6" y2="1">
        <stop offset="0" stop-color="var(--photo-violet)"/>
        <stop offset="0.45" stop-color="var(--photo-pink)"/>
        <stop offset="0.7" stop-color="var(--photo-violet)"/>
        <stop offset="1" stop-color="var(--photo-deep)"/>
      </linearGradient>
    </defs>
    <path class="front-photo" role="img" aria-label="Fireworks bursting over a city waterfront at night with a flag in the background" fill="url(#photoTone)"
          d="M0,0 H200 L292,162 Q304,180 292,196 L150,359 H0 Z"/>
    <path class="front-panel-grey" fill="var(--panel-grey)"
          d="M214,0 H503 V45 L392,165 Q378,182 358,182 H330 Q318,182 312,172 Z"/>
    <path class="front-panel-red" fill="var(--brand-red)"
          d="M503,58 L402,166 Q390,180 402,194 L503,296 Z"/>
    <path class="front-panel-blue" fill="var(--brand-blue)"
          d="M172,359 L292,210 Q302,198 316,198 H332 Q346,198 360,208 L503,312 V359 Z"/>
  </svg>

  <div class="brand">
    <span class="brand__dot"></span>
    <span class="brand__name">Brightwater Legal</span>
  </div>

  <h1 class="greeting">
    <span class="greeting__line--small">HAPPY</span>
    <span class="greeting__line--large">4TH OF JULY</span>
  </h1>
</section>

<section class="postcard postcard--back" aria-label="Postcard back">
  <svg class="postcard__art" viewBox="0 0 503 360" preserveAspectRatio="none" aria-hidden="true">
    <path class="back-panel-grey" fill="var(--panel-grey)"
          d="M0,0 H112 L274,160 Q284,178 274,196 L112,360 H0 Z"/>
    <path class="back-panel-edge" fill="none" stroke="var(--brand-blue)" stroke-width="3.5"
          d="M117,0 L279,160 Q289,178 279,196 L117,360"/>
  </svg>

  <div class="brand">
    <span class="brand__dot"></span>
    <span class="brand__name">Brightwater Legal</span>
  </div>

  <div class="thanks">
    <h2 class="thanks__title">Thank You</h2>
    <p class="thanks__sub">For Being A Valued Client!</p>
  </div>

  <p class="wish">Stay Safe And Enjoy Your<br>Independence Day Celebrations!</p>

  <div class="stamp-box"></div>
  <div class="address-line address-line--1"></div>
  <div class="address-line address-line--2"></div>
  <div class="address-line address-line--3"></div>
</section>

</body>
</html>
```